Business card for Northland's Blue Wagon.

Good day i am looking for a business card design for my business.
The name of the business is Northland's Blue Wagon. It is a van rental business that provides a driver and helper to the customer. Customer have use to van for small moves, studio or 1 bedroom, Moving furniture like couch or kitchen cabinets.
We are available evenings, weekends and holidays.
the means to contact us is by phone at 628-947-2071; By emails at Oakridge@northlandsbluewagon.net; or by social media, Facebook and Instagram.
You can see attached pictures of the van and or logo.

```html
<!DOCTYPE html>
<html lang="en">
<head>
<meta charset="utf-8">
<title>Northland's Blue Wagon – Business Card</title>
<link rel="stylesheet" href="https://fonts.googleapis.com/css2?family=Montserrat:wght@400;500;600&display=swap">
<style>
  :root {
    --backdrop: #6b6b6b;
    --card: #ffffff;
    --brand-red: #d42027;
    --ink: #1b1b1b;
    --faint: #fbe9ea;
  }
  html, body {
    margin: 0;
    width: 1200px;
    height: 1200px;
    overflow: hidden;
    background: var(--backdrop);
    font-family: "Montserrat", sans-serif;
  }
  .card {
    position: absolute;
    left: 166px;
    width: 868px;
    height: 508px;
    background: var(--card);
    box-shadow: 0 6px 12px rgba(0,0,0,0.35);
    overflow: hidden;
  }
  .card--front { top: 74px; }
  .card--back { top: 629px; background: var(--brand-red); }

  .front-decoration {
    position: absolute;
    left: 420px;
    top: 0;
    width: 448px;
    height: 370px;
    background: radial-gradient(ellipse at 55% 40%, var(--faint) 0%, rgba(251,233,234,0.5) 45%, rgba(255,255,255,0) 72%);
  }

  .wordmark {
    position: absolute;
    color: var(--brand-red);
    font-weight: 600;
    text-align: center;
    line-height: 1.15;
    letter-spacing: 0.02em;
  }
  .card--front .wordmark {
    left: 60px;
    top: 150px;
    width: 290px;
    font-size: 34px;
  }

  .contact-list {
    position: absolute;
    right: 52px;
    top: 330px;
    margin: 0;
    padding: 0;
    list-style: none;
  }
  .contact-item {
    display: flex;
    justify-content: flex-end;
    align-items: center;
    height: 40px;
    font-size: 25px;
    color: var(--ink);
  }
  .contact-item--web { font-weight: 600; }
  .contact-icon {
    width: 16px;
    height: 16px;
    margin-left: 18px;
    flex: none;
  }

  .back-panel {
    position: absolute;
    left: 30px;
    top: 30px;
    right: 28px;
    bottom: 29px;
    background: var(--card);
    border-radius: 32px;
    display: flex;
    align-items: center;
    justify-content: center;
  }
  .card--back .wordmark {
    position: static;
    font-size: 44px;
    width: 420px;
  }
</style>
</head>
<body>
  <section class="card card--front">
    <div class="front-decoration" role="img" aria-label="Faint decorative brand swirl"></div>
    <div class="wordmark">Northland's Blue Wagon</div>
    <ul class="contact-list">
      <li class="contact-item">628-947-2071
        <svg class="contact-icon" viewBox="0 0 16 16" aria-hidden="true"><path fill="#d42027" d="M3.2 1.5l2.3 2.6-1.3 1.6c.9 2 2.4 3.5 4.4 4.4l1.6-1.3 2.6 2.3-1.2 2.1C6.8 13.2 2.8 9.2 1.1 2.7z"/></svg>
      </li>
      <li class="contact-item">Oakridge@northlandsbluewagon.net
        <svg class="contact-icon" viewBox="0 0 16 16" aria-hidden="true"><rect x="1" y="3" width="14" height="10" rx="1.5" fill="#d42027"/><path d="M1.5 4l6.5 5 6.5-5" stroke="#fff" stroke-width="1.3" fill="none"/></svg>
      </li>
      <li class="contact-item contact-item--web">northlandsbluewagon.net
        <svg class="contact-icon" viewBox="0 0 16 16" aria-hidden="true"><circle cx="8" cy="8" r="6.5" fill="none" stroke="#d42027" stroke-width="1.5"/><ellipse cx="8" cy="8" rx="2.8" ry="6.5" fill="none" stroke="#d42027" stroke-width="1.2"/><path d="M1.5 8h13M2.5 5h11M2.5 11h11" stroke="#d42027" stroke-width="1.1"/></svg>
      </li>
    </ul>
  </section>

  <section class="card card--back">
    <div class="back-panel">
      <div class="wordmark">Northland's Blue Wagon</div>
    </div>
  </section>
</body>
</html>
```